Brivan Learning Web Design Project

Who We are:
Brivan Learning is education information portal/ magazine, providing information about the Chinese and International education markets. Our aim is to help school principals improve there curriculum, and parents in understanding this curriculum.

Project Brief:
The site will include education news updates, educational services, curriculum developments and overseas study. We hope the site represents the cross cultural bridge between the west and east. The site will cover both the Sciences and Arts.

Note:
The logo design competition is also underway so we only need the website design

What We want:
This competition is for Design only no coding!
Design a home page based on Template 1,2 or 3. I only need to select one.
The design of an article page.

Optional
Design a Microsoft Windows metro style splash page.

Sites We like:
http://www.qz.com.cn/wordsparrow/default.aspx
http://www.velmaracademicpost.co.uk/
http://pvro.orbalinkstudy.net/

Template Explanations:
Template 1-
The main information has a dynamic sliding category view that when clicked displays the relevant info.
In addition to the main upper menu it also has a left hand sliding menu that pops out on click or gesture

Template 2-
Has limited number of Articles most of the menus are drop downs from the top menu

Template 3-
No Top menu

Target Market(s)

Teachers, principals and parents

Industry/Entity Type

Education

Requirements
Should not have
• kindergarten preschool feel

```html
<!DOCTYPE html>
<html lang="en">
<head>
<meta charset="utf-8">
<title>Brivan Learning</title>
<link rel="stylesheet" href="https://fonts.googleapis.com/css2?family=Open+Sans:wght@400;600;700&display=swap">
<style>
:root{
  --red:#e2231a;
  --red-dark:#c81d15;
  --navy:#1d3f7a;
  --text:#555;
  --dark:#222;
  --board:#3a3a3a;
  --board-bar:#262626;
  --line:#cfcfcf;
  --ad-bg:#1e1f24;
  --white:#fff;
}
*{margin:0;padding:0;box-sizing:border-box}
html,body{width:1200px;height:1200px;overflow:hidden;background:var(--white);font-family:"Open Sans",Arial,sans-serif}
.page{position:relative;width:1200px;height:1200px}
.top-rule{position:absolute;left:0;top:0;width:1200px;height:5px;background:var(--red)}
.brand{position:absolute;left:120px;top:28px;display:flex;flex-direction:column;align-items:flex-start;gap:10px}
.brand-mark{width:60px;height:60px;border-radius:50%;background:var(--red);margin-left:64px}
.brand-name{font-size:22px;font-weight:700;color:var(--navy);white-space:nowrap;line-height:28px}
.search{position:absolute;left:779px;top:60px;width:300px;height:35px;border:1px solid #ccc;background:var(--white)}
.search svg{position:absolute;right:18px;top:9px}
.main-nav{position:absolute;left:120px;top:160px;width:960px;height:40px;background:var(--red);display:flex;border-bottom:1px solid var(--red-dark)}
.main-nav a{color:var(--white);text-decoration:none;font-size:14px;font-weight:600;display:flex;align-items:center;justify-content:center;border-right:1px solid var(--red-dark);height:100%}
.main-nav a:last-child{border-right:0}
.hero{position:absolute;left:120px;top:211px;width:960px;height:380px;background:linear-gradient(120deg,#e9dcc0 0%,#c99a73 35%,#6e8d7b 70%,#d7b88a 100%)}
.hero-dots{position:absolute;left:460px;top:356px;display:flex;gap:5px}
.hero-dots span{width:10px;height:10px;border-radius:50%;background:#666;opacity:.6}
.hero-dots span:first-child{background:#333;opacity:.9}
.article{position:absolute;top:602px;width:330px}
.article .thumb{width:330px;height:140px}
.article .stars{margin-top:19px;display:flex;gap:1px}
.article h3{margin-top:16px;font-size:14.5px;font-weight:600;color:var(--red);line-height:20px}
.article time{display:block;margin-top:1px;font-size:11px;color:var(--dark);line-height:16px}
.article p{margin-top:6px;font-size:13px;line-height:18px;color:var(--text)}
.rule{position:absolute;left:120px;top:903px;width:690px;height:5px;border-top:1px solid var(--line);border-bottom:1px solid var(--line)}
.connect{position:absolute;left:181px;top:936px;font-size:22px;color:var(--red);font-weight:400}
.social{position:absolute;left:411px;top:936px;display:flex;gap:19px}
.social span{width:34px;height:34px;border-radius:50%;box-shadow:0 1px 3px rgba(0,0,0,.35)}
.ad{position:absolute;left:840px;top:602px;width:240px;height:400px;background:var(--ad-bg);overflow:hidden}
.ad-art{position:absolute;left:0;top:95px;width:240px;height:285px;background:linear-gradient(160deg,#2b2c34 0%,#3b5fae 35%,#8a3a6a 65%,#2b2c34 100%)}
.ad-head{position:absolute;left:4px;top:10px;color:#e8e8e8;font-size:16px;line-height:22px;white-space:nowrap}
.ad-head b{display:block;font-size:27px;font-weight:400;line-height:32px}
.ad-btn{position:absolute;left:107px;top:72px;width:122px;height:25px;border-radius:13px;background:var(--red);color:var(--white);font-size:13px;display:flex;align-items:center;padding-left:13px}
.ad-title{position:absolute;left:12px;top:200px;font-size:54px;font-weight:700;color:#dfe3e8;white-space:nowrap}
.ad-maker{position:absolute;right:8px;bottom:5px;font-size:12px;font-weight:700;color:var(--white)}
.footer{position:absolute;left:0;top:1012px;width:1200px;height:156px;background:radial-gradient(ellipse at 50% 40%,#4a4a4a,var(--board))}
.footer ul{position:absolute;top:17px;list-style:none}
.footer li{font-size:13px;font-weight:600;color:var(--white);line-height:24px}
.chalk{position:absolute;left:1066px;top:78px;width:84px;height:58px;background:linear-gradient(135deg,#f3f3f3,#d9c3ae);border-radius:6px;opacity:.85}
.copyright{position:absolute;left:0;top:1168px;width:1200px;height:32px;background:var(--board-bar);color:#ddd;font-size:13px;text-align:center;line-height:34px;padding-right:56px}
</style>
</head>
<body>
<div class="page">
  <div class="top-rule"></div>

  <header class="brand">
    <span class="brand-mark"></span>
    <span class="brand-name">Brivan Learning</span>
  </header>

  <div class="search">
    <svg width="18" height="16" viewBox="0 0 18 16"><circle cx="6" cy="6" r="4" fill="none" stroke="#e2231a" stroke-width="2"/><line x1="9" y1="9" x2="16" y2="14" stroke="#e2231a" stroke-width="3" stroke-linecap="round"/></svg>
  </div>

  <nav class="main-nav">
    <a style="width:116px">HOME</a>
    <a style="width:145px">ABOUT US</a>
    <a style="width:115px">BLOG</a>
    <a style="width:138px">COURSES</a>
    <a style="width:110px">BLOG</a>
    <a style="width:177px">TESTIMONIALS</a>
    <a style="width:159px">CONTATC US</a>
  </nav>

  <section class="hero" role="img" aria-label="Photo of a smiling group of students holding books and folders in a classroom">
    <div class="hero-dots"><span></span><span></span><span></span></div>
  </section>

  <article class="article" style="left:120px">
    <div class="thumb" role="img" aria-label="Photo of students working at laptops in a computer class" style="background:linear-gradient(100deg,#f2ece6,#b7867a 45%,#e5e7ea)"></div>
    <div class="stars">
      <svg width="78" height="14" viewBox="0 0 78 14"><g fill="#f5a623" stroke="#c9791a" stroke-width=".6"><polygon id="s" points="7,1 8.8,5 13,5.3 9.8,8.1 10.8,12.4 7,10.1 3.2,12.4 4.2,8.1 1,5.3 5.2,5"/><use href="#s" x="15.5"/><use href="#s" x="31"/><use href="#s" x="46.5"/><use href="#s" x="62"/></g></svg>
    </div>
    <h3>Lorem ipsum dolor sit amet, consectetur</h3>
    <time>16 July, 2013</time>
    <p>Lorem ipsum dolor sit amet, consectetur adipisicing elit, sed do eiusmod tempor incididunt ut labore et dolore magna aliqua.</p>
  </article>

  <article class="article" style="left:480px">
    <div class="thumb" role="img" aria-label="Close-up photo of a student in a classroom" style="background:linear-gradient(90deg,#d9a78a,#c08a6e 40%,#b8312a 75%,#7a6058)"></div>
    <div class="stars">
      <svg width="78" height="14" viewBox="0 0 78 14"><g fill="#f5a623" stroke="#c9791a" stroke-width=".6"><polygon id="s2" points="7,1 8.8,5 13,5.3 9.8,8.1 10.8,12.4 7,10.1 3.2,12.4 4.2,8.1 1,5.3 5.2,5"/><use href="#s2" x="15.5"/><use href="#s2" x="31"/><use href="#s2" x="46.5"/><use href="#s2" x="62"/></g></svg>
    </div>
    <h3>Lorem ipsum dolor sit amet, consectetur</h3>
    <time>16 July, 2013</time>
    <p>Lorem ipsum dolor sit amet, consectetur adipisicing elit, sed do eiusmod tempor incididunt ut labore et dolore magna aliqua.</p>
  </article>

  <div class="rule"></div>

  <div class="connect">CONNECT WITH US</div>
  <div class="social">
    <span style="background:#3b5998"></span>
    <span style="background:#2aa9e0"></span>
    <span style="background:#1b7ab8"></span>
    <span style="background:#d3201c"></span>
    <span style="background:#c0392b"></span>
    <span style="background:#f58a1f"></span>
  </div>

  <aside class="ad">
    <div class="ad-art" role="img" aria-label="Colourful abstract software artwork"></div>
    <div class="ad-head">modern differential geometry<b>for Calcula</b></div>
    <div class="ad-btn">explore now</div>
    <div class="ad-title">Orbis 2</div>
    <div class="ad-maker">Quantiva inc.</div>
  </aside>

  <footer class="footer">
    <ul style="left:187px"><li>Home</li><li>About Us</li><li>Subjects</li><li>My Courses</li><li>Contact Us</li></ul>
    <ul style="left:427px"><li>Computer Science</li><li>Accounting</li><li>History</li><li>Drama</li><li>Asia</li></ul>
    <ul style="left:669px"><li>Commerce</li><li>English</li><li>USA</li><li>Asia</li><li>Commerce</li></ul>
    <ul style="left:908px"><li>Commerce</li><li>English</li><li>USA</li><li>Asia</li><li>Commerce</li></ul>
    <div class="chalk" role="img" aria-label="Two pieces of chalk lying on the board"></div>
  </footer>

  <div class="copyright">©2013 Brivan Learning &nbsp;| All Rihts Reserved.</div>
</div>
</body>
</html>
```